New Solo Law Office Needs Business Card/Letterhead Design

I am starting a solo law office called "Law Office of Brian Kolmer, PLLC" in Tucson, Arizona. I will be doing criminal defense trial work. More than a logo with any sort of icon, I am really just looking for the name of the company to be displayed in a sleek, minimalist but interesting sort of way, with a format and font type that communicates professionalism. It can be in color, but doesn't have to be, and I am thinking blue and/or red accents colors. I'd like it to convey that I am passionate, dependable and willing to fight. For the business card, I envision sort of higher quality card material, and maybe some embossing or raised print. I will want to include my company name, name, phone and fax numbers, email and website addresses. For the letterhead, I will want to be able to use the same sort of font/formatting design as on the business card.
Industry/Entity Type
Business
Contact Information for Business Card
Law Office of Brian Kolmer, PLLC
Brian Kolmer
brian@kolmer-law.example
www.kolmer-law.example
(I do not yet have an established phone or fax number, so please put in some place holder numbers for the formatting, and I can add the actual numbers in before I print.)
Colors
Designer to choose colors to be used in the design.
Look and feel
Each slider illustrates characteristics of the customer's brand and the style your logo design should communicate.

```html
<!DOCTYPE html>
<html lang="en">
<head>
<meta charset="utf-8">
<title>Law Office of Brian Kolmer, PLLC – Business Card</title>
<link href="https://fonts.googleapis.com/css2?family=Raleway:wght@500;600;700&display=swap" rel="stylesheet">
<style>
  :root {
    --accent-red: #f2534f;
    --navy: #243f8f;
    --ink: #4a4a4c;
    --rule: #5a5a5c;
    --paper: #ffffff;
    --white: #ffffff;
  }
  * { margin: 0; padding: 0; box-sizing: border-box; }
  html, body {
    width: 1200px; height: 686px; overflow: hidden;
    background: var(--paper);
  }
  .card {
    position: relative; width: 1200px; height: 686px;
    background: var(--paper);
    font-family: "Raleway", sans-serif;
    color: var(--ink);
  }
  .top-band {
    position: absolute; left: 0; top: 0; width: 100%; height: 51px;
    background: var(--accent-red);
  }
  .emblem-ring {
    position: absolute; left: 209px; top: 160px; width: 252px; height: 252px;
  }
  .identity {
    position: absolute; left: 489px; top: 200px; width: 480px;
  }
  .firm-name {
    font-weight: 700; font-size: 40px; line-height: 50px;
    letter-spacing: 1.5px; text-transform: uppercase;
  }
  .attorney-name {
    margin-top: 8px;
    font-weight: 700; font-size: 35px; line-height: 44px;
    letter-spacing: 1.5px; text-transform: uppercase;
  }
  .designation {
    font-weight: 700; font-size: 25px; line-height: 34px;
    letter-spacing: 1px;
  }
  .identity-rule {
    margin-top: 14px; width: 479px; height: 2px; background: var(--rule);
  }
  .contact-band {
    position: absolute; left: 0; top: 503px; width: 100%; height: 183px;
    background: var(--navy);
    color: var(--white);
  }
  .contact-col {
    position: absolute; top: 36px;
    display: flex; flex-direction: column; gap: 20px;
  }
  .contact-col.phones { left: 194px; }
  .contact-col.online { left: 522px; }
  .contact-item {
    display: flex; align-items: center; gap: 12px;
    font-weight: 500; font-size: 33px; line-height: 38px; letter-spacing: 0.3px;
  }
  .contact-icon { width: 34px; height: 34px; flex: none; }
  .contact-divider {
    position: absolute; left: 488px; top: 40px; width: 2px; height: 92px;
    background: var(--white);
  }
</style>
</head>
<body>
<div class="card">
  <div class="top-band"></div>

  <svg class="emblem-ring" viewBox="0 0 252 252" aria-hidden="true">
    <circle cx="126" cy="126" r="116" fill="none" stroke="var(--ink)" stroke-width="16"/>
  </svg>

  <div class="identity">
    <h1 class="firm-name">Law Office of<br>Brian Kolmer, PLLC</h1>
    <p class="attorney-name">Brian Kolmer</p>
    <p class="designation">Designation here</p>
    <div class="identity-rule"></div>
  </div>

  <div class="contact-band">
    <div class="contact-col phones">
      <div class="contact-item">
        <svg class="contact-icon" viewBox="0 0 34 34" aria-hidden="true">
          <circle cx="17" cy="17" r="15.5" fill="none" stroke="currentColor" stroke-width="2"/>
          <path d="M11.5 9.5c1-.8 2.2-.6 2.8.4l1.3 2.3c.4.8.2 1.7-.5 2.2l-1 .7c.8 2.1 2.4 3.8 4.4 4.8l.8-1c.6-.7 1.5-.8 2.2-.3l2.2 1.5c.9.6 1 1.9.2 2.8-1.6 1.8-3.5 1.9-5.8.7-3.5-1.9-6.2-5-7.4-8.7-.6-2-.3-4 .8-5.4z" fill="currentColor"/>
        </svg>
        <span>91-55501482</span>
      </div>
      <div class="contact-item">
        <svg class="contact-icon" viewBox="0 0 34 34" aria-hidden="true">
          <circle cx="17" cy="17" r="15.5" fill="none" stroke="currentColor" stroke-width="2"/>
          <rect x="12" y="8.5" width="10" height="5" fill="currentColor"/>
          <rect x="8.5" y="13" width="17" height="8" rx="1.5" fill="currentColor"/>
          <rect x="12" y="18.5" width="10" height="7" fill="var(--navy)" stroke="currentColor" stroke-width="1.6"/>
        </svg>
        <span>555-0189233</span>
      </div>
    </div>

    <div class="contact-divider"></div>

    <div class="contact-col online">
      <div class="contact-item">
        <svg class="contact-icon" viewBox="0 0 34 34" aria-hidden="true">
          <circle cx="17" cy="17" r="15.5" fill="none" stroke="currentColor" stroke-width="2"/>
          <rect x="9" y="11.5" width="16" height="11" rx="1" fill="currentColor"/>
          <path d="M9.5 12.5l7.5 6 7.5-6" fill="none" stroke="var(--navy)" stroke-width="1.6"/>
        </svg>
        <span>brian@kolmer-law.example</span>
      </div>
      <div class="contact-item">
        <svg class="contact-icon" viewBox="0 0 34 34" aria-hidden="true">
          <circle cx="17" cy="17" r="15.5" fill="none" stroke="currentColor" stroke-width="2"/>
          <g fill="none" stroke="currentColor" stroke-width="1.5">
            <circle cx="17" cy="17" r="9"/>
            <ellipse cx="17" cy="17" rx="4" ry="9"/>
            <path d="M8 17h18M9.5 12.5h15M9.5 21.5h15"/>
          </g>
        </svg>
        <span>www.kolmer-law.example</span>
      </div>
    </div>
  </div>
</div>
</body>
</html>
```